business card deign

Logo needs the following on it.
1. attached logo
2. Tagline - "Whatever chills the cans or lifts the mood...we make it!"
3. Name- Delia Fenwick, Founder and CPO
4. Address - 418 E. Harlow Avenue, Ste 2204, Tampa, FL. 33719
5. Phone - 720.555.0187

```html
<!DOCTYPE html>
<html lang="en">
<head>
<meta charset="utf-8">
<title>Tolvaro business card</title>
<link href="https://fonts.googleapis.com/css2?family=Roboto+Condensed:wght@400;700&family=Arimo:wght@400&display=swap" rel="stylesheet">
<style>
  :root {
    --backdrop: #727272;
    --card-dark: #262626;
    --card-dark-hi: #2f2f2f;
    --card-light: #ffffff;
    --ink: #333333;
    --ink-soft: #6b6b6b;
    --ghost: #ebebeb;
    --white: #ffffff;
  }
  * { margin: 0; padding: 0; box-sizing: border-box; }
  html, body {
    width: 1200px; height: 1000px; overflow: hidden;
    background: var(--backdrop);
  }
  .canvas { position: relative; width: 1200px; height: 1000px; }
  .card {
    position: absolute; width: 352px; height: 612px;
    border-radius: 20px; overflow: hidden;
  }
  .card--back { left: 203px; top: 203px; background: var(--card-dark); }
  .card--front { left: 603px; top: 197px; background: var(--card-light); }

  .pattern-field {
    position: absolute; inset: 0;
    background: linear-gradient(180deg, var(--card-dark-hi) 0%, var(--card-dark) 100%);
  }
  .tagline {
    position: absolute; left: 0; right: 0; top: 476px;
    text-align: center; color: var(--white);
    font-family: "Arimo", Arial, sans-serif; font-size: 19px; line-height: 26px;
  }

  .brand {
    position: absolute; left: 0; right: 0; top: 100px;
    display: flex; flex-direction: column; align-items: center; gap: 14px;
  }
  .brand-dot { width: 100px; height: 100px; border-radius: 50%; background: var(--ink); }
  .brand-name {
    font-family: "Roboto Condensed", Arial Narrow, sans-serif; font-weight: 700;
    font-size: 32px; letter-spacing: 14px; padding-left: 14px; color: var(--ink);
  }
  .person {
    position: absolute; left: 0; right: 0; top: 318px; text-align: center;
  }
  .person-name {
    font-family: "Roboto Condensed", Arial Narrow, sans-serif; font-weight: 700;
    font-size: 30px; line-height: 34px; color: var(--ink);
  }
  .person-title {
    font-family: "Arimo", Arial, sans-serif; font-size: 13px;
    letter-spacing: 1.6px; color: var(--ink-soft); margin-top: 1px;
  }
  .contact-icons {
    position: absolute; left: 0; right: 0; top: 379px;
    display: flex; justify-content: center; gap: 5px;
  }
  .contact-icons svg { width: 32px; height: 32px; display: block; }
  .contact-lines {
    position: absolute; left: 0; right: 0; top: 419px; text-align: center;
    font-family: "Arimo", Arial, sans-serif; font-size: 17.5px; line-height: 22px;
    color: var(--ink-soft);
  }
  .ghost-name {
    position: absolute; left: 0; right: 0; top: 544px; text-align: center; white-space: nowrap;
    font-family: "Roboto Condensed", Arial Narrow, sans-serif; font-weight: 700;
    font-size: 68px; letter-spacing: 26px; color: var(--ghost);
  }
</style>
</head>
<body>
<main class="canvas">
  <section class="card card--back">
    <div class="pattern-field" role="img" aria-label="Repeating tonal brand pattern on dark card back"></div>
    <p class="tagline">Whatever chills the cans or<br>lifts the mood...we make it!</p>
  </section>

  <section class="card card--front">
    <div class="brand">
      <span class="brand-dot"></span>
      <span class="brand-name">TOLVARO</span>
    </div>
    <div class="person">
      <h1 class="person-name">DELIA FENWICK</h1>
      <p class="person-title">FOUNDER AND CPO</p>
    </div>
    <div class="contact-icons">
      <svg viewBox="0 0 32 32" aria-label="Phone">
        <circle cx="16" cy="16" r="16" fill="#333"/>
        <path d="M11.5 9.5l2.4-.4 1.3 3.2-1.6 1.2c.7 1.6 2 2.9 3.6 3.6l1.2-1.6 3.2 1.3-.4 2.4c-.2.8-1 1.3-1.8 1.2-4.4-.6-8-4.2-8.6-8.6-.1-.8.4-1.6 1.2-1.8z" fill="#fff"/>
      </svg>
      <svg viewBox="0 0 32 32" aria-label="Location">
        <circle cx="16" cy="16" r="16" fill="#333"/>
        <path d="M16 8.5c-3 0-5.2 2.3-5.2 5.1 0 3.7 5.2 9.9 5.2 9.9s5.2-6.2 5.2-9.9c0-2.8-2.2-5.1-5.2-5.1z" fill="#fff"/>
        <circle cx="16" cy="13.6" r="1.9" fill="#333"/>
      </svg>
    </div>
    <div class="contact-lines">
      <p>(720) 555-0187</p>
      <p>418 E. Harlow Avenue, Ste 2204</p>
      <p>Tampa, FL. 33719</p>
    </div>
    <span class="ghost-name">TOLVARO</span>
  </section>
</main>
</body>
</html>
```